refurbishment of diamond cut alloy wheels

we need to design a flyer that will catch the eye of the customer to refurbish diamond cut alloy wheels. we refurbish the wheels by using the latest CNC machine to precision cut and resurface the wheel. we would like before and after pictures of maybe Kelvaron, DXT, Orsa wheels to give it a prestige look. The final design should communicate an expensive look and providing a good image for the business. The colours that I would like to use is black and red which should make the flyer stand out. The logo must sit on a black background without the wordings of specialists in HJ, Orsa etc and also without servicing, diagnostics etc as well. This flyer is just to communicate refurbishment of alloy wheels to high standard.

Target Market(s)

any members of the public and car dealerships

Industry/Entity Type

Automotive

Colors

Designer to choose colors to be used in the design.

Requirements
Must have
• Wow factor with great images of wheels
Nice to have
• Maybe on the front of the flyer it has a picture of a wheel and then on the back of the flyer it has before and after pictures to show how just how incredible it is to refurbish wheels
Should not have
• other makes of wheels apart from DXT, Orsa, and any other high end makes of vehicles wheels

```html
<!DOCTYPE html>
<html lang="en">
<head>
<meta charset="utf-8">
<title>Halden Wheelworks – Alloy Wheel Refurbishment Flyer</title>
<link rel="stylesheet" href="https://fonts.googleapis.com/css2?family=Oswald:wght@400;500;600&family=Open+Sans:wght@400;600;700&display=swap">
<style>
  :root{
    --bg:#e4e1dc;
    --black:#0b0b0c;
    --panel:#1a1a1c;
    --panel-edge:#3a3a3e;
    --red:#d41a1f;
    --red-dark:#8e0c10;
    --silver:#c9c9cc;
    --silver-dark:#7d7d82;
    --white:#ffffff;
    --grey-text:#d8d8d8;
  }
  *{box-sizing:border-box;margin:0;padding:0}
  html,body{width:1200px;height:806px;overflow:hidden}
  body{background:var(--bg);font-family:"Open Sans",Arial,sans-serif;position:relative}

  .flyer{position:absolute;top:50px;width:500px;height:708px;background:var(--black);overflow:hidden;
    box-shadow:0 4px 14px rgba(0,0,0,.25)}
  .flyer--front{left:69px}
  .flyer--back{left:631px}

  .hero-photo{position:absolute;left:0;top:0;width:500px;height:400px}
  .hero-photo--car{background:radial-gradient(ellipse at 40% 62%,#b8161c 0%,#6a0a0d 28%,#1c1c1f 55%,#0b0b0c 80%)}
  .hero-photo--wheels{height:320px;background:radial-gradient(ellipse at 50% 38%,#9a9aa0 0%,#4a4a50 35%,#1a1a1d 65%,#0b0b0c 90%)}

  .brand{position:absolute;left:0;right:0;top:40px;display:flex;justify-content:center;align-items:center;gap:10px}
  .brand__mark{width:30px;height:30px;background:var(--red)}
  .brand__name{font-family:"Oswald",sans-serif;font-weight:600;font-size:34px;color:var(--white);text-transform:uppercase;letter-spacing:1px}

  .chevron{position:absolute;left:0;width:500px}

  .badge{position:absolute}
  .badge__text{position:absolute;inset:0;display:flex;align-items:center;justify-content:center;text-align:center;
    font-family:"Oswald",sans-serif;font-weight:500;font-size:11px;line-height:1.35;color:var(--white);text-transform:uppercase}

  .headline{position:absolute;left:0;right:0;top:450px;text-align:center;font-family:"Oswald",sans-serif;font-weight:500;
    font-size:22px;color:var(--white);text-transform:uppercase;letter-spacing:.3px}

  .intro{position:absolute;left:16px;top:492px;width:300px;color:var(--grey-text);font-size:10.4px;line-height:1.5;text-align:justify}
  .intro p+p{margin-top:12px}

  .compare{position:absolute;left:336px;width:146px;height:62px;border:1px solid var(--panel-edge);border-radius:6px;
    background:radial-gradient(circle at 55% 50%,#d4d4d8 0%,#8d8d92 40%,#2a2a2d 75%)}
  .compare--before{top:489px}
  .compare--after{top:558px}
  .compare__tag{position:absolute;left:4px;top:4px;background:var(--red);color:var(--white);font-family:"Oswald",sans-serif;
    font-size:10px;font-weight:600;padding:1px 8px;border-radius:2px;text-transform:uppercase}

  .services{position:absolute;left:14px;top:398px;width:474px;display:grid;grid-template-columns:1fr 1fr;gap:10px 16px}
  .service{position:relative;height:110px;border:1px solid var(--panel-edge);border-radius:8px;background:linear-gradient(180deg,#222225,#101012);overflow:hidden}
  .service__copy{position:absolute;left:10px;top:12px;width:140px;z-index:1}
  .service__title{font-family:"Oswald",sans-serif;font-weight:500;font-size:10.5px;line-height:1.6;color:var(--white);text-transform:uppercase}
  .service__body{margin-top:8px;font-size:7.4px;line-height:1.4;color:var(--grey-text)}
  .service__photo{position:absolute;right:0;top:0;width:80px;height:100%;
    background:radial-gradient(circle at 60% 50%,#bcbcc0 0%,#6c6c72 38%,#1a1a1d 75%)}

  .contact-cta{position:absolute;left:0;right:0;top:636px;text-align:center}
  .contact-cta__lead{font-family:"Oswald",sans-serif;font-weight:500;font-size:11px;color:var(--red);text-transform:uppercase}
  .contact-cta__web{margin-top:3px;font-size:10px;color:var(--white)}

  .footer-bar{position:absolute;left:0;right:0;bottom:0;height:36px;background:#151517;display:flex;align-items:center}
  .footer-bar__address{position:absolute;left:0;top:0;height:36px;width:330px;background:var(--red);
    clip-path:polygon(0 0,100% 0,92% 100%,0 100%);display:flex;align-items:center;gap:7px;padding-left:16px;
    color:var(--white);font-size:10px;font-weight:600}
  .footer-bar__phone{position:absolute;right:14px;top:0;height:36px;display:flex;align-items:center;gap:8px;
    font-family:"Oswald",sans-serif;font-weight:500;font-size:20px;color:var(--white);letter-spacing:.5px}
</style>
</head>
<body>

<section class="flyer flyer--front">
  <div class="hero-photo hero-photo--car" role="img" aria-label="Red sports car with diamond cut alloy wheels in a dark studio"></div>

  <div class="brand">
    <span class="brand__mark"></span>
    <span class="brand__name">Halden Wheelworks</span>
  </div>

  <svg class="chevron" style="top:280px" height="190" viewBox="0 280 500 190" aria-hidden="true">
    <polygon points="0,285 250,400 500,285 500,470 0,470" fill="#0b0b0c"/>
    <polygon points="0,318 250,420 500,318 500,345 250,452 0,345" fill="var(--silver)"/>
    <polygon points="0,345 250,452 500,345 500,352 250,460 0,352" fill="var(--silver-dark)"/>
    <polygon points="250,392 500,300 500,322 250,418" fill="var(--red)"/>
    <polygon points="250,418 500,322 500,330 250,426" fill="var(--red-dark)"/>
  </svg>

  <div class="badge" style="left:22px;top:296px;width:130px;height:130px">
    <svg width="130" height="130" viewBox="0 0 130 130" aria-hidden="true">
      <circle cx="65" cy="65" r="58" fill="var(--red)" stroke="var(--red)" stroke-width="12" stroke-dasharray="4 4"/>
      <circle cx="65" cy="65" r="52" fill="var(--red-dark)" opacity=".35"/>
    </svg>
    <div class="badge__text">We offer<br>local collection<br>and delivery</div>
  </div>

  <h1 class="headline">Refurbishment of diamond cut alloy wheels</h1>

  <div class="intro">
    <p>If you are looking to refresh the look of your car but don't want the expense of new alloys, with a wide range of limited edition colours to choose from why not consider customising and refurbishing your existing alloys?</p>
    <p>We use the latest technology to refurbish the wheels to a high standard to look like new. We also carry out bodywork using water based paints with our in house paint scheme ensuring a perfect colour match.</p>
  </div>

  <div class="compare compare--before" role="img" aria-label="Alloy wheel before refurbishment"><span class="compare__tag">Before</span></div>
  <div class="compare compare--after" role="img" aria-label="Alloy wheel after refurbishment"><span class="compare__tag">After</span></div>

  <div class="contact-cta">
    <p class="contact-cta__lead">If you need premier alloy refurbishment services in Ashcombe, please contact us:</p>
    <p class="contact-cta__web">www.haldenwheelworks.co.uk | Nico@haldenwheelworks.co.uk</p>
  </div>

  <div class="footer-bar">
    <div class="footer-bar__address">
      <svg width="10" height="14" viewBox="0 0 10 14" aria-hidden="true"><path d="M5 0a5 5 0 0 0-5 5c0 3.5 5 9 5 9s5-5.5 5-9a5 5 0 0 0-5-5zm0 7a2 2 0 1 1 0-4 2 2 0 0 1 0 4z" fill="#fff"/></svg>
      14B Fernlow Road, Ashcombe, Berkshire, AC2 7LT
    </div>
    <div class="footer-bar__phone">
      <svg width="18" height="18" viewBox="0 0 24 24" aria-hidden="true"><circle cx="12" cy="12" r="11" fill="none" stroke="#fff" stroke-width="2"/><path d="M8.5 6.5l2 2-1.2 1.5c.8 1.7 2 2.9 3.7 3.7l1.5-1.2 2 2-1.3 1.8c-4-.6-7.6-4.2-8.2-8.2z" fill="#fff"/></svg>
      01632 960418
    </div>
  </div>
</section>

<section class="flyer flyer--back">
  <div class="hero-photo hero-photo--wheels" role="img" aria-label="Three premium alloy wheels in black and silver finishes"></div>

  <svg class="chevron" style="top:230px" height="190" viewBox="0 230 500 190" aria-hidden="true">
    <polygon points="0,235 250,340 500,235 500,420 0,420" fill="#0b0b0c"/>
    <polygon points="0,262 250,362 500,262 500,289 250,394 0,289" fill="var(--silver)"/>
    <polygon points="0,289 250,394 500,289 500,296 250,402 0,296" fill="var(--silver-dark)"/>
    <polygon points="250,334 500,244 500,266 250,360" fill="var(--red)"/>
    <polygon points="250,360 500,266 500,274 250,368" fill="var(--red-dark)"/>
  </svg>

  <div class="badge" style="left:36px;top:268px;width:110px;height:110px">
    <svg width="110" height="110" viewBox="0 0 110 110" aria-hidden="true">
      <circle cx="55" cy="55" r="48" fill="var(--red)" stroke="var(--red)" stroke-width="12" stroke-dasharray="4 4"/>
      <circle cx="55" cy="55" r="43" fill="var(--red-dark)" opacity=".35"/>
    </svg>
    <div class="badge__text" style="font-size:10px">We offer<br>local collection<br>and delivery</div>
  </div>

  <div class="services">
    <article class="service">
      <div class="service__copy">
        <h2 class="service__title">Refurbish old or new<br>alloy wheels to perfection</h2>
        <p class="service__body">We can also supply replacement split rim outer rims, stainless steel wheel trims, titanium and alloy wheel bolts.</p>
      </div>
      <div class="service__photo" role="img" aria-label="Worn silver alloy wheel"></div>
    </article>
    <article class="service">
      <div class="service__copy">
        <h2 class="service__title">Pure styling with a<br>touch of class...</h2>
        <p class="service__body">Using an advanced refurbishment technique, we offer unique color-coding.</p>
      </div>
      <div class="service__photo" role="img" aria-label="Dark colour-coded alloy wheel"></div>
    </article>
    <article class="service">
      <div class="service__copy">
        <h2 class="service__title">We can fix, respray &amp; repair<br>damaged alloy wheels</h2>
        <p class="service__body">With our advanced technology, alloy wheel bolts, and studs.</p>
      </div>
      <div class="service__photo" role="img" aria-label="Damaged alloy wheel being repaired"></div>
    </article>
    <article class="service">
      <div class="service__copy">
        <h2 class="service__title">Fast affordable friendly<br>service</h2>
        <p class="service__body">We cater to all locations in and around Colnbrook, Windsor, Hayes, Hounslow, Staines, Ascot and Ashford.</p>
      </div>
      <div class="service__photo" role="img" aria-label="Polished multi-spoke alloy wheel"></div>
    </article>
  </div>

  <div class="contact-cta">
    <p class="contact-cta__lead">If you need premier alloy refurbishment services in Ashcombe, please contact us:</p>
    <p class="contact-cta__web">www.haldenwheelworks.co.uk | Nico@haldenwheelworks.co.uk</p>
  </div>

  <div class="footer-bar">
    <div class="footer-bar__address">
      <svg width="10" height="14" viewBox="0 0 10 14" aria-hidden="true"><path d="M5 0a5 5 0 0 0-5 5c0 3.5 5 9 5 9s5-5.5 5-9a5 5 0 0 0-5-5zm0 7a2 2 0 1 1 0-4 2 2 0 0 1 0 4z" fill="#fff"/></svg>
      14B Fernlow Road, Ashcombe, Berkshire, AC2 7LT
    </div>
    <div class="footer-bar__phone">
      <svg width="18" height="18" viewBox="0 0 24 24" aria-hidden="true"><circle cx="12" cy="12" r="11" fill="none" stroke="#fff" stroke-width="2"/><path d="M8.5 6.5l2 2-1.2 1.5c.8 1.7 2 2.9 3.7 3.7l1.5-1.2 2 2-1.3 1.8c-4-.6-7.6-4.2-8.2-8.2z" fill="#fff"/></svg>
      01632 960418
    </div>
  </div>
</section>

</body>
</html>
```